Business Card Design Project - IT Company

Kestrafield Information Technology Solutions
We are an Information Technology Company. We provide computer services to commercial companies. We would like a new card full color front and back with bleeding edge.
We have a logo that you can use or if you want to come up with a new logo that is fine too.
Our colors are mostly Maroon and black but be creative.
Sample Information
Brent R Okafor
4812 W Saguaro Ridge Drive
Suite 410
Dunmere Flats, AZ 85099
O: 602.914.2037
C: 602.468.1290
24/7: 888.914.2037
bokafor@kestrafield.example
www.kestrafield.example
Target Market(s)
Business of all sizes
Industry/Entity Type
Computer
Requirements
Must have
- Bleeding edge
full color on both sides

```html
<!DOCTYPE html>
<html lang="en">
<head>
<meta charset="utf-8">
<title>Kestrafield Business Cards</title>
<link rel="stylesheet" href="https://fonts.googleapis.com/css2?family=Jost:wght@400&family=Tinos&family=Arimo:wght@400;700&display=swap">
<style>
  :root {
    --backdrop: #e4e4e4;
    --card: #ffffff;
    --maroon: #850009;
    --ink: #222222;
    --tagline: #4a4a4a;
  }
  * { margin: 0; padding: 0; box-sizing: border-box; }
  html, body { width: 1200px; height: 900px; overflow: hidden; }
  body {
    background: radial-gradient(ellipse at 55% 45%, #f7f7f7 0%, var(--backdrop) 70%, #d2d2d2 100%);
    position: relative;
  }
  .card {
    position: absolute;
    width: 580px;
    height: 331px;
    background: var(--card);
    box-shadow: 0 6px 14px rgba(0,0,0,0.22);
    overflow: hidden;
  }
  .card-front { left: 160px; top: 95px; }
  .card-back { left: 440px; top: 470px; }
  .bleed-band {
    position: absolute;
    left: 0; right: 0; bottom: 0;
    height: 26px;
    background: var(--maroon);
  }
  .brand { position: absolute; }
  .brand-name {
    font-family: 'Jost', sans-serif;
    font-weight: 400;
    color: var(--ink);
    letter-spacing: 0.08em;
    text-transform: uppercase;
    line-height: 1;
    white-space: nowrap;
  }
  .brand-tagline {
    font-family: 'Tinos', serif;
    color: var(--tagline);
    white-space: nowrap;
    line-height: 1;
  }
  .card-front .brand { left: 108px; top: 120px; }
  .card-front .brand-name { font-size: 50px; }
  .card-front .brand-tagline { font-size: 23px; margin-top: 6px; }
  .card-back .brand { left: 28px; top: 115px; }
  .card-back .brand-name { font-size: 31px; }
  .card-back .brand-tagline { font-size: 14.5px; margin-top: 4px; }
  .divider {
    position: absolute;
    left: 286px; top: 28px;
    width: 2px; height: 265px;
    background: linear-gradient(to bottom, rgba(133,0,9,0.2), var(--maroon) 30%, rgba(133,0,9,0.05));
  }
  .contact {
    position: absolute;
    left: 318px; top: 100px;
    font-family: 'Arimo', sans-serif;
    color: var(--maroon);
  }
  .contact-name { font-size: 20px; font-weight: 700; margin-bottom: 14px; }
  .contact-lines { list-style: none; font-size: 13px; line-height: 1.32; }
</style>
</head>
<body>
  <section class="card card-front" aria-label="Card front">
    <div class="brand">
      <div class="brand-name">Kestrafield</div>
      <div class="brand-tagline">Information Technology Solutions</div>
    </div>
    <div class="bleed-band"></div>
  </section>

  <section class="card card-back" aria-label="Card back">
    <div class="brand">
      <div class="brand-name">Kestrafield</div>
      <div class="brand-tagline">Information Technology Solutions</div>
    </div>
    <div class="divider"></div>
    <div class="contact">
      <div class="contact-name">Brent R Okafor</div>
      <ul class="contact-lines">
        <li>4812 W Saguaro Ridge Drive</li>
        <li>Suite 410</li>
        <li>Dunmere Flats, AZ 85099</li>
        <li>O: 602.914.2037</li>
        <li>C: 602.468.1290</li>
        <li>24/7: 888.914.2037</li>
        <li>bokafor@kestrafield.example</li>
        <li>www.kestrafield.example</li>
      </ul>
    </div>
    <div class="bleed-band"></div>
  </section>
</body>
</html>
```